New web design for a service provider in the medical field

We are looking for a new design for our website. We are a company that repairs and sells medical endoscopes. Our customers include doctors and hospitals. Our current website can be found at https://lumenfix.example/en/lumenfix-english.
We need a new web design (without programming) for the following 3 pages:
-Startpage https://lumenfix.example/en/lumenfix-english/
-Used endoscopes https://lumenfix.example/en/used-endoscopes/
-Purchase https://lumenfix.example/en/purchase/
The design should be modern and stylish.
The blue color of the logo should be reflected on the page, but not too intrusive.
I have uploaded the images from the header. If more images are needed, let me know and I will upload them.

Target Market(s)
Doctors and hospitals

```html
<!DOCTYPE html>
<html lang="en">
<head>
<meta charset="utf-8">
<title>LumenFix – Purchase</title>
<link rel="stylesheet" href="https://fonts.googleapis.com/css2?family=Lexend:wght@500;600;700&family=Montserrat:wght@400;500&display=swap">
<style>
:root{
  --blue:#0a62b8;
  --navy:#0a4ea3;
  --sky:#3aaef0;
  --ink:#1b1b1f;
  --text:#3a3a42;
  --muted:#8b8f98;
  --line:#cfd6df;
  --pale:#eef6fc;
  --footer:#e8f4fd;
  --bar:#b7e0f8;
}
*{box-sizing:border-box;margin:0;padding:0}
html,body{width:1200px;height:2572px;overflow:hidden}
body{position:relative;background:#fff;font-family:"Montserrat",sans-serif;color:var(--text)}
.abs{position:absolute}
a{color:inherit}
.heading{font-family:"Lexend",sans-serif;font-weight:600;color:var(--ink);letter-spacing:.3px}
.btn{position:absolute;display:flex;align-items:center;justify-content:center;gap:8px;background:var(--blue);color:#fff;border-radius:24px;font-size:14px;font-weight:500;text-decoration:none}
.hero-bg{left:0;top:0;width:1200px;height:660px;background:linear-gradient(180deg,#e4f1fb 0,#f1f7fc 40%,#e8f2fa 100%)}
.brand{left:172px;top:44px;font-family:"Montserrat",sans-serif;font-weight:500;font-size:22px;color:#3b3d44;display:flex;align-items:center;gap:8px}
.brand .dot{width:10px;height:10px;border-radius:50%;background:var(--sky)}
.topbar{left:0;top:0;width:1200px;height:120px}
.toplinks{left:424px;top:22px;display:flex;gap:12px;font-size:12.5px;color:#fff;align-items:center}
.toplinks a{text-decoration:underline}
.toplinks span{display:flex;align-items:center;gap:8px}
.lang{background:#0d3d80;border-radius:12px;padding:3px 6px;font-weight:600;font-size:11px}
.nav{left:365px;top:74px;display:flex;gap:18px;font-size:13.5px;color:#fff;align-items:center}
.hero-title{left:162px;top:226px;font-size:33px;line-height:50px}
.hero-title em{font-style:normal;color:var(--blue)}
.scroll{left:575px;top:463px;font-size:12px;color:#333;text-align:center}
.photo{border-radius:50%}
.sell-title{left:465px;top:800px;font-size:24px;line-height:36px;width:560px}
.sell-copy{left:465px;top:885px;width:575px;font-size:13.5px;line-height:23px}
.sell-copy p+p{margin-top:13px}
.replace{left:0;top:1242px;width:1200px;text-align:center;font-size:24px}
.card{left:161px;top:1408px;width:879px;height:697px;background:#fff;border-radius:10px;box-shadow:0 2px 14px rgba(30,70,120,.09)}
.sect{position:absolute;left:31px;font-family:"Lexend",sans-serif;font-weight:600;font-size:17.5px;color:var(--blue)}
.field{position:absolute;width:398px;height:38px;border:1px solid var(--line);border-radius:19px;font-size:13.5px;color:var(--muted);padding:0 20px;display:flex;align-items:center;justify-content:space-between}
.c1{left:31px}.c2{left:452px}
.hint{position:absolute;left:452px;top:476px;font-size:11.5px;color:var(--muted)}
.consent{position:absolute;left:31px;top:535px;width:820px;font-size:13.5px;line-height:23px;padding-left:24px}
.consent i{position:absolute;left:0;top:5px;width:14px;height:14px;border:1px solid var(--line);border-radius:2px}
.consent a{color:var(--blue)}
.foot-bg{left:0;top:2210px;width:1200px;height:320px}
.fcol h4{font-family:"Lexend",sans-serif;font-weight:600;font-size:18px;color:var(--blue);margin-bottom:14px}
.fcol{position:absolute;top:2306px;font-size:13px;color:#2c2c34;line-height:30px}
.divider{position:absolute;top:2306px;height:200px;border-left:1px dashed #a9b3bf}
.fl{display:flex;gap:14px;align-items:flex-start;line-height:20px;margin-bottom:10px}
.social{position:absolute;top:2403px;width:31px;height:31px;border-radius:50%;background:var(--navy);display:flex;align-items:center;justify-content:center}
.copy{left:0;top:2530px;width:1200px;height:42px;background:var(--bar);text-align:center;line-height:42px;font-size:12.5px;color:#2c3440}
</style>
</head>
<body>

<div class="abs hero-bg"></div>
<svg class="abs" style="left:0;top:380px" width="1200" height="300" viewBox="0 380 1200 300" aria-hidden="true">
  <defs>
    <linearGradient id="waveGrad" x1="0" x2="1">
      <stop offset="0" stop-color="#3ab4f5"/><stop offset=".55" stop-color="#1a7fd6"/><stop offset="1" stop-color="#0a4ea3"/>
    </linearGradient>
  </defs>
  <path d="M0 505 C200 440 420 470 600 520 C780 570 980 560 1200 390 L1200 580 C1000 680 760 670 560 600 C380 540 180 520 0 630 Z" fill="url(#waveGrad)"/>
  <path d="M8 528 C190 470 400 490 590 535 C690 558 760 565 830 560 C720 575 620 560 560 545 C380 500 200 490 8 528 Z" fill="#fff"/>
</svg>

<svg class="abs topbar" viewBox="0 0 1200 120" aria-hidden="true">
  <path d="M390 0 H1200 V63 H420 Z" fill="var(--navy)"/>
  <path d="M365 64 H1200 V106 H365 A21 21 0 0 1 365 64 Z" fill="var(--blue)"/>
  <path d="M470 106 C520 118 580 112 620 106 Z" fill="var(--blue)"/>
</svg>
<div class="abs brand"><span class="dot"></span>LumenFix</div>
<div class="abs toplinks">
  <a href="#">Pick-Up Order</a><a href="#">About us</a><a href="#">Contact us</a>
  <span><svg width="14" height="14" viewBox="0 0 24 24"><path fill="#fff" d="M6.6 10.8a15 15 0 0 0 6.6 6.6l2.2-2.2c.3-.3.7-.4 1-.2 1.1.4 2.3.6 3.6.6.6 0 1 .4 1 1V20c0 .6-.4 1-1 1A17 17 0 0 1 3 4c0-.6.4-1 1-1h3.5c.6 0 1 .4 1 1 0 1.3.2 2.5.6 3.6.1.3 0 .7-.2 1z"/></svg>+49 4000 555 120-0</span>
  <span><svg width="14" height="12" viewBox="0 0 24 20"><path fill="#fff" d="M2 2h20v16H2z"/><path fill="var(--navy)" d="M2 2l10 8 10-8v2l-10 8L2 4z"/></svg>info@lumenfix.example</span>
  <span class="lang">DE&nbsp; EN</span>
</div>
<nav class="abs nav">
  <svg width="18" height="17" viewBox="0 0 24 22"><path fill="#fff" d="M12 1 1 11h3v10h6v-6h4v6h6V11h3z"/></svg>
  <span>Endoscope Repair</span><span>Used Endoscopes</span><span>Endoscopy Systems</span><span>Endoscopy Accessories</span><span>Purchase</span>
</nav>

<h1 class="abs heading hero-title">SUSTAINABLE AND<br><em>ECONOMICAL</em></h1>
<a class="btn" href="#" style="left:163px;top:331px;width:150px;height:45px">CONTACT US <svg width="16" height="10" viewBox="0 0 16 10"><path d="M0 5h14M10 1l4 4-4 4" stroke="#fff" stroke-width="1.6" fill="none"/></svg></a>
<div class="abs scroll">SCROLL<br><svg width="10" height="16" viewBox="0 0 10 16"><path d="M5 0v14M1 10l4 4 4-4" stroke="#333" stroke-width="1.4" fill="none"/></svg></div>
<svg class="abs" style="left:635px;top:130px" width="390" height="390" aria-hidden="true"><circle cx="195" cy="195" r="193" fill="none" stroke="#3b8ad6" stroke-dasharray="4 4"/><circle cx="195" cy="195" r="180" fill="#fff"/></svg>
<div class="abs photo" role="img" aria-label="Endoscopy video processor and light source units" style="left:668px;top:163px;width:340px;height:322px;background:linear-gradient(135deg,#ff6f4f 0,#f3b8a8 35%,#c9cfd8 60%,#2f3442 100%)"></div>

<svg class="abs" style="left:-110px;top:668px" width="510" height="505" aria-hidden="true"><circle cx="257" cy="252" r="250" fill="none" stroke="#3b8ad6" stroke-dasharray="4 4"/><circle cx="257" cy="252" r="235" fill="#f4f5f7"/></svg>
<div class="abs photo" role="img" aria-label="Close-up of endoscope control knobs and valve ports" style="left:-85px;top:695px;width:442px;height:436px;background:radial-gradient(circle at 40% 35%,#6c6f75 0,#3a3c41 45%,#b9bcc2 100%)"></div>
<svg class="abs" style="left:1128px;top:810px" width="72" height="200" aria-hidden="true"><circle cx="100" cy="100" r="86" fill="none" stroke="#f0f0f0" stroke-width="26"/></svg>
<h2 class="abs heading sell-title">DO YOU WANT TO SELL YOUR ENDOSCOPE YOU? ARE AT THE RIGHT ADRESS!</h2>
<div class="abs sell-copy">
  <p>We are always interested in buying used endoscopes, accessories and peripherals from Orvion, Pellax and Fujara at fair conditions. We can promise you an objective offer with a clear conscience! Use the form below to offer us your device! If you want to have several devices checked, one of our technicians will usually come to you for the check. We also check defective and incomplete devices!</p>
  <p>We would be happy to take a look at your device!</p>
</div>

<h2 class="abs heading replace">ARE YOU LOOKING TO REPLACE YOUR FOR SALE DEVICE?</h2>
<a class="btn" href="#" style="left:327px;top:1292px;width:547px;height:45px">REABROWSE OUR RANGE OF EXCELLENT USED EQUIPMENT!D MORE <svg width="16" height="10" viewBox="0 0 16 10"><path d="M0 5h14M10 1l4 4-4 4" stroke="#fff" stroke-width="1.6" fill="none"/></svg></a>

<form class="abs card">
  <div class="sect" style="top:28px">Personal Informations</div>
  <div class="field c1" style="top:66px">Salutation* <svg width="10" height="6"><path d="M1 1l4 4 4-4" stroke="#555" fill="none"/></svg></div>
  <div class="field c2" style="top:66px">Co. / Dr. Off.*</div>
  <div class="field c1" style="top:116px">Surname</div>
  <div class="field c2" style="top:116px">Firstname</div>
  <div class="field c1" style="top:168px">Email*</div>
  <div class="field c2" style="top:168px">Telephone</div>
  <div class="sect" style="top:236px">Informations About The Device</div>
  <div class="field c1" style="top:274px">Brand* <svg width="10" height="6"><path d="M1 1l4 4 4-4" stroke="#555" fill="none"/></svg></div>
  <div class="field c2" style="top:274px">Model* <svg width="10" height="6"><path d="M1 1l4 4 4-4" stroke="#555" fill="none"/></svg></div>
  <div class="field c1" style="top:325px">Defects / Damage</div>
  <div class="field c2" style="top:325px">Asking Price</div>
  <div class="sect" style="top:393px">Remarks And Picture</div>
  <div class="field c1" style="top:431px;height:90px;border-radius:8px;align-items:flex-start;padding-top:10px">Remarks</div>
  <div class="field c2" style="top:431px;padding-right:2px">Upload Picture <span class="btn" style="position:relative;width:108px;height:32px;font-size:13px">BROWSE <svg width="16" height="10" viewBox="0 0 16 10"><path d="M0 5h14M10 1l4 4-4 4" stroke="#fff" stroke-width="1.6" fill="none"/></svg></span></div>
  <div class="hint">Allowed formats jpg, jpeg, png or bmp maximum file size 4 MB</div>
  <div class="consent"><i></i>I have read the <a href="#">privacy policy</a> and accept it. I agree above input will be transmitted to LumenFix GmbH to get in contact with me respectively to process my request and store all needed informations. Neither a transfer to third parties will happen, nor a use for advertising purposes by LumenFix GmbH!</div>
  <span class="btn" style="left:390px;top:623px;width:99px;height:45px">SEND <svg width="16" height="10" viewBox="0 0 16 10"><path d="M0 5h14M10 1l4 4-4 4" stroke="#fff" stroke-width="1.6" fill="none"/></svg></span>
</form>

<svg class="abs foot-bg" viewBox="0 2210 1200 320" aria-hidden="true">
  <defs><linearGradient id="footGrad" x1="0" x2="1"><stop offset="0" stop-color="#3ab4f5"/><stop offset="1" stop-color="#0a4ea3"/></linearGradient></defs>
  <path d="M0 2290 C350 2180 850 2180 1200 2290 V2530 H0 Z" fill="var(--footer)"/>
  <path d="M0 2280 C350 2190 850 2180 1200 2270 V2290 C850 2195 350 2200 0 2290 Z" fill="url(#footGrad)"/>
</svg>
<div class="fcol" style="left:161px"><h4>Quick Links</h4>Endoscope Repair<br>Used Endoscopes<br>Endoscopy Systems<br>Endoscopy Accessories<br>Purchase</div>
<div class="divider" style="left:347px"></div>
<div class="fcol" style="left:386px"><h4>Contact Us</h4>
  <div class="fl"><svg width="14" height="18" viewBox="0 0 14 18"><path fill="var(--blue)" d="M7 0a7 7 0 0 0-7 7c0 5 7 11 7 11s7-6 7-11a7 7 0 0 0-7-7zm0 10a3 3 0 1 1 0-6 3 3 0 0 1 0 6z"/></svg><span>Lindenweg 12 20095<br>Musterstadt Germany</span></div>
  <div class="fl"><svg width="14" height="14" viewBox="0 0 24 24"><path fill="var(--blue)" d="M6.6 10.8a15 15 0 0 0 6.6 6.6l2.2-2.2c.3-.3.7-.4 1-.2 1.1.4 2.3.6 3.6.6.6 0 1 .4 1 1V20c0 .6-.4 1-1 1A17 17 0 0 1 3 4c0-.6.4-1 1-1h3.5c.6 0 1 .4 1 1 0 1.3.2 2.5.6 3.6.1.3 0 .7-.2 1z"/></svg><span>+49 4000 555 120-0</span></div>
  <div class="fl"><svg width="14" height="14" viewBox="0 0 14 14"><rect x="1" y="4" width="12" height="9" rx="1" fill="var(--blue)"/><rect x="4" y="1" width="6" height="4" fill="var(--blue)"/></svg><span>+49 4000 555 120-1</span></div>
  <div class="fl"><svg width="14" height="12" viewBox="0 0 24 20"><path fill="var(--blue)" d="M2 2h20v16H2z"/><path fill="#fff" d="M2 2l10 8 10-8v2l-10 8L2 4z"/></svg><span>info@lumenfix.example</span></div>
</div>
<div class="divider" style="left:620px"></div>
<div class="fcol" style="left:671px"><h4>Opening Hours</h4>
  <div class="fl"><svg width="18" height="18" viewBox="0 0 18 18"><rect x="1" y="3" width="16" height="14" rx="2" fill="none" stroke="var(--blue)" stroke-width="1.5"/><path d="M1 7h16M5 1v4M13 1v4" stroke="var(--blue)" stroke-width="1.5"/></svg><span>Monday – Friday<br><span style="line-height:28px">08:00 – 20:00</span></span></div>
</div>
<div class="divider" style="left:850px"></div>
<div class="abs brand" style="left:895px;top:2338px"><span class="dot"></span>LumenFix</div>
<a class="social" href="#" style="left:929px" aria-label="Share">
  <svg width="14" height="14" viewBox="0 0 14 14"><circle cx="11" cy="2.5" r="2" fill="#fff"/><circle cx="11" cy="11.5" r="2" fill="#fff"/><circle cx="3" cy="7" r="2" fill="#fff"/><path d="M11 2.5 3 7l8 4.5" stroke="#fff" stroke-width="1.2" fill="none"/></svg>
</a>
<a class="social" href="#" style="left:971px" aria-label="Website">
  <svg width="14" height="14" viewBox="0 0 14 14"><circle cx="7" cy="7" r="6" fill="none" stroke="#fff" stroke-width="1.3"/><ellipse cx="7" cy="7" rx="2.6" ry="6" fill="none" stroke="#fff" stroke-width="1.1"/><path d="M1 7h12" stroke="#fff" stroke-width="1.1"/></svg>
</a>
<div class="abs copy">© LumenFix MedicalDevices Repairs - 2022. All Rights Reserved.</div>

</body>
</html>
```